Wandkalender für Bio-Wollstoffe in A!
sehr gute und selbständige Arbeit trotz zeitbedingt wenig Input von uns. Herzlichen Dank!
Zielgruppe
Wir verkaufen Bio Wollstoffe zum Nähen. Unsere Zielgruppe sind also ökologisch bewußte kreative Näherinnen.
Aufgabenstellung
Wir möchten einen Wandkalender in DinA1 fertigen. Fotos werden von uns geliefert und können bunt zwischen die Monate verteilt werden.
Technisch haben wir von der Druckerei folgende Vorgaben:
Endformat: DIN A4 21,0 x 29,7 cm
Format offen: DIN A1 59,4 x 84,1 cm
Umfang: einseitig bedruckt
Satz/Repro: druckfähige PDF-Daten geliefert, wir
senden Ihnen einen Bildschirmsoftproof
Druck/Farben: 4/0 farbig Skala
Papier: 135 g/qm Bilderdruck Matt

```html
<!DOCTYPE html>
<html lang="en">
<head>
<meta charset="utf-8">
<title>Wall Calendar 2020</title>
<link href="https://fonts.googleapis.com/css2?family=Oswald:wght@400;500;600&family=Montserrat:wght@400;500;600&display=swap" rel="stylesheet">
<style>
  :root{
    --blue-deep:#7fa2ba;
    --blue-soft:#a9c5d5;
    --blue-tab:#a4bfcf;
    --paper:#e3eaee;
    --paper-light:#eef2f4;
    --ink:#2b333b;
    --ink-dark:#2e363e;
    --sunday:#9ab4c4;
    --white:#ffffff;
    --dash:#d8e6ee;
  }
  *{box-sizing:border-box;margin:0;padding:0}
  html,body{width:869px;height:1200px;overflow:hidden;background:#fff}
  .poster{position:relative;width:869px;height:1200px;background:var(--white);font-family:"Montserrat",sans-serif;color:var(--ink)}

  .year-block{position:absolute;left:0;top:0;width:250px;height:126px;background:var(--blue-deep);display:flex;align-items:center;justify-content:center}
  .year{font-family:"Oswald",sans-serif;font-weight:600;font-size:84px;color:var(--white);letter-spacing:1px;line-height:1;margin-top:-4px}
  .notes{position:absolute;left:0;top:126px;width:250px;height:294px;background:var(--blue-soft)}
  .notes .line{position:absolute;height:0;border-top:1px dashed var(--dash);right:35px}

  .collage{position:absolute;left:253px;top:0;width:616px;height:420px;background:var(--white)}
  .photo{position:absolute}

  .calendar{position:absolute;left:0;top:420px;width:869px;height:654px;background:linear-gradient(180deg,var(--paper) 0%,var(--paper-light) 60%,var(--paper) 100%)}
  .month{position:absolute;width:180px}
  .tab{height:50px;background:var(--blue-tab);border-top-right-radius:12px;display:flex;align-items:center;padding-left:16px;font-family:"Oswald",sans-serif;color:var(--white)}
  .tab .num{font-size:30px;font-weight:500;line-height:1;padding-right:10px;border-right:1.5px solid var(--white)}
  .tab .name{font-size:18px;font-weight:400;text-transform:uppercase;padding-left:10px;margin-top:4px}
  .dow{display:grid;grid-template-columns:repeat(7,1fr);height:16px;background:var(--ink-dark);font-size:8.5px;font-weight:600;color:var(--white);align-items:center;text-align:center}
  .dow span:first-child{background:var(--blue-tab);height:16px;line-height:16px;color:var(--white);font-weight:500}
  .days{display:grid;grid-template-columns:repeat(7,1fr);grid-auto-rows:19px;font-size:10px;font-weight:500;text-align:center;align-items:center;padding-top:4px}
  .days i{font-style:normal}
  .o0 i:first-child{grid-column-start:1}.o0 i:nth-child(7n+1){color:var(--sunday)}
  .o1 i:first-child{grid-column-start:2}.o1 i:nth-child(7n+7){color:var(--sunday)}
  .o2 i:first-child{grid-column-start:3}.o2 i:nth-child(7n+6){color:var(--sunday)}
  .o3 i:first-child{grid-column-start:4}.o3 i:nth-child(7n+5){color:var(--sunday)}
  .o4 i:first-child{grid-column-start:5}.o4 i:nth-child(7n+4){color:var(--sunday)}
  .o5 i:first-child{grid-column-start:6}.o5 i:nth-child(7n+3){color:var(--sunday)}
  .o6 i:first-child{grid-column-start:7}.o6 i:nth-child(7n+2){color:var(--sunday)}

  .footer{position:absolute;left:0;top:1074px;width:869px;height:126px;background:var(--ink-dark);display:flex;align-items:center}
  .brand{width:250px;height:126px;background:var(--blue-soft);display:flex;align-items:center;justify-content:center;color:var(--white);font-size:18px;font-weight:400;letter-spacing:.5px}
  .contact{display:flex;align-items:center;gap:5px;font-size:10.5px;color:var(--white);position:absolute;top:57px}
  .contact svg{width:9px;height:9px;fill:var(--blue-tab)}
</style>
</head>
<body>
<main class="poster">
  <div class="year-block"><span class="year">2020</span></div>
  <div class="notes">
    <span class="line" style="left:83px;top:57px"></span>
    <span class="line" style="left:37px;top:86px"></span>
    <span class="line" style="left:37px;top:116px"></span>
    <span class="line" style="left:37px;top:146px"></span>
    <span class="line" style="left:37px;top:176px"></span>
    <span class="line" style="left:37px;top:205px"></span>
  </div>

  <section class="collage">
    <div class="photo" role="img" aria-label="Cat lying on a wooden floor beside a knitted garment" style="left:7px;top:6px;width:128px;height:228px;background:linear-gradient(160deg,#d9cdbf,#b8a591)"></div>
    <div class="photo" role="img" aria-label="Colourful wool shorts hanging on a clothesline in a garden" style="left:140px;top:6px;width:247px;height:134px;background:linear-gradient(180deg,#b8c0a6,#7d8c62)"></div>
    <div class="photo" role="img" aria-label="Child holding a sunflower" style="left:392px;top:6px;width:105px;height:69px;background:linear-gradient(180deg,#8b97a8,#565c60)"></div>
    <div class="photo" role="img" aria-label="Children sitting together on a garden bench" style="left:503px;top:6px;width:105px;height:134px;background:linear-gradient(180deg,#9fae94,#a07a58)"></div>
    <div class="photo" role="img" aria-label="Wool garment next to a bicycle wheel" style="left:140px;top:146px;width:120px;height:87px;background:linear-gradient(135deg,#4f5965,#b8b060)"></div>
    <div class="photo" role="img" aria-label="Family in wool clothing walking on a log" style="left:265px;top:146px;width:122px;height:170px;background:linear-gradient(180deg,#7d9460,#8b6b55)"></div>
    <div class="photo" role="img" aria-label="Small child in an orange hooded outfit on gravel" style="left:392px;top:78px;width:105px;height:156px;background:linear-gradient(180deg,#b48a62,#8e5b3a)"></div>
    <div class="photo" role="img" aria-label="Legs in blue wool trousers resting on a table outdoors" style="left:503px;top:146px;width:105px;height:123px;background:linear-gradient(180deg,#c6d0d4,#4e6a8a)"></div>
    <div class="photo" role="img" aria-label="Child in red skirt and leg warmers climbing a wall" style="left:7px;top:238px;width:128px;height:174px;background:linear-gradient(180deg,#b0a8a0,#8a4656)"></div>
    <div class="photo" role="img" aria-label="Woman in a grey wool top jumping outdoors" style="left:140px;top:238px;width:120px;height:174px;background:linear-gradient(180deg,#c9ccc8,#8a8478)"></div>
    <div class="photo" role="img" aria-label="Two children in wool ponchos in a garden" style="left:392px;top:238px;width:105px;height:78px;background:linear-gradient(180deg,#6b7558,#5c4634)"></div>
    <div class="photo" role="img" aria-label="Wool skirt in grey and mustard laid flat" style="left:503px;top:273px;width:105px;height:72px;background:linear-gradient(135deg,#e0ddd6,#b8952e)"></div>
    <div class="photo" role="img" aria-label="Toddlers in red wool clothes on a sandy beach" style="left:265px;top:320px;width:232px;height:92px;background:linear-gradient(180deg,#7a7670,#5a4e48)"></div>
    <div class="photo" role="img" aria-label="Children in red wool outfits running on grass" style="left:503px;top:349px;width:105px;height:63px;background:linear-gradient(180deg,#6b8a4a,#4e7a38)"></div>
  </section>

  <section class="calendar">
    <article class="month o3" style="left:30px;top:47px">
      <header class="tab"><span class="num">01</span><span class="name">January</span></header>
      <div class="dow"><span>Su</span><span>Mo</span><span>Tu</span><span>We</span><span>Th</span><span>Fr</span><span>Sa</span></div>
      <div class="days"><i>1</i><i>2</i><i>3</i><i>4</i><i>5</i><i>6</i><i>7</i><i>8</i><i>9</i><i>10</i><i>11</i><i>12</i><i>13</i><i>14</i><i>15</i><i>16</i><i>17</i><i>18</i><i>19</i><i>20</i><i>21</i><i>22</i><i>23</i><i>24</i><i>25</i><i>26</i><i>27</i><i>28</i><i>29</i><i>30</i><i>31</i></div>
    </article>
    <article class="month o6" style="left:240px;top:47px">
      <header class="tab"><span class="num">02</span><span class="name">February</span></header>
      <div class="dow"><span>Su</span><span>Mo</span><span>Tu</span><span>We</span><span>Th</span><span>Fr</span><span>Sa</span></div>
      <div class="days"><i>1</i><i>2</i><i>3</i><i>4</i><i>5</i><i>6</i><i>7</i><i>8</i><i>9</i><i>10</i><i>11</i><i>12</i><i>13</i><i>14</i><i>15</i><i>16</i><i>17</i><i>18</i><i>19</i><i>20</i><i>21</i><i>22</i><i>23</i><i>24</i><i>25</i><i>26</i><i>27</i><i>28</i><i>29</i></div>
    </article>
    <article class="month o0" style="left:450px;top:47px">
      <header class="tab"><span class="num">03</span><span class="name">March</span></header>
      <div class="dow"><span>Su</span><span>Mo</span><span>Tu</span><span>We</span><span>Th</span><span>Fr</span><span>Sa</span></div>
      <div class="days"><i>1</i><i>2</i><i>3</i><i>4</i><i>5</i><i>6</i><i>7</i><i>8</i><i>9</i><i>10</i><i>11</i><i>12</i><i>13</i><i>14</i><i>15</i><i>16</i><i>17</i><i>18</i><i>19</i><i>20</i><i>21</i><i>22</i><i>23</i><i>24</i><i>25</i><i>26</i><i>27</i><i>28</i><i>29</i><i>30</i><i>31</i></div>
    </article>
    <article class="month o3" style="left:660px;top:47px">
      <header class="tab"><span class="num">04</span><span class="name">April</span></header>
      <div class="dow"><span>Su</span><span>Mo</span><span>Tu</span><span>We</span><span>Th</span><span>Fr</span><span>Sa</span></div>
      <div class="days"><i>1</i><i>2</i><i>3</i><i>4</i><i>5</i><i>6</i><i>7</i><i>8</i><i>9</i><i>10</i><i>11</i><i>12</i><i>13</i><i>14</i><i>15</i><i>16</i><i>17</i><i>18</i><i>19</i><i>20</i><i>21</i><i>22</i><i>23</i><i>24</i><i>25</i><i>26</i><i>27</i><i>28</i><i>29</i><i>30</i></div>
    </article>

    <article class="month o5" style="left:30px;top:247px">
      <header class="tab"><span class="num">05</span><span class="name">May</span></header>
      <div class="dow"><span>Su</span><span>Mo</span><span>Tu</span><span>We</span><span>Th</span><span>Fr</span><span>Sa</span></div>
      <div class="days"><i>1</i><i>2</i><i>3</i><i>4</i><i>5</i><i>6</i><i>7</i><i>8</i><i>9</i><i>10</i><i>11</i><i>12</i><i>13</i><i>14</i><i>15</i><i>16</i><i>17</i><i>18</i><i>19</i><i>20</i><i>21</i><i>22</i><i>23</i><i>24</i><i>25</i><i>26</i><i>27</i><i>28</i><i>29</i><i>30</i><i>31</i></div>
    </article>
    <article class="month o1" style="left:240px;top:247px">
      <header class="tab"><span class="num">06</span><span class="name">June</span></header>
      <div class="dow"><span>Su</span><span>Mo</span><span>Tu</span><span>We</span><span>Th</span><span>Fr</span><span>Sa</span></div>
      <div class="days"><i>1</i><i>2</i><i>3</i><i>4</i><i>5</i><i>6</i><i>7</i><i>8</i><i>9</i><i>10</i><i>11</i><i>12</i><i>13</i><i>14</i><i>15</i><i>16</i><i>17</i><i>18</i><i>19</i><i>20</i><i>21</i><i>22</i><i>23</i><i>24</i><i>25</i><i>26</i><i>27</i><i>28</i><i>29</i><i>30</i></div>
    </article>
    <article class="month o3" style="left:450px;top:247px">
      <header class="tab"><span class="num">07</span><span class="name">July</span></header>
      <div class="dow"><span>Su</span><span>Mo</span><span>Tu</span><span>We</span><span>Th</span><span>Fr</span><span>Sa</span></div>
      <div class="days"><i>1</i><i>2</i><i>3</i><i>4</i><i>5</i><i>6</i><i>7</i><i>8</i><i>9</i><i>10</i><i>11</i><i>12</i><i>13</i><i>14</i><i>15</i><i>16</i><i>17</i><i>18</i><i>19</i><i>20</i><i>21</i><i>22</i><i>23</i><i>24</i><i>25</i><i>26</i><i>27</i><i>28</i><i>29</i><i>30</i><i>31</i></div>
    </article>
    <article class="month o6" style="left:660px;top:247px">
      <header class="tab"><span class="num">08</span><span class="name">August</span></header>
      <div class="dow"><span>Su</span><span>Mo</span><span>Tu</span><span>We</span><span>Th</span><span>Fr</span><span>Sa</span></div>
      <div class="days"><i>1</i><i>2</i><i>3</i><i>4</i><i>5</i><i>6</i><i>7</i><i>8</i><i>9</i><i>10</i><i>11</i><i>12</i><i>13</i><i>14</i><i>15</i><i>16</i><i>17</i><i>18</i><i>19</i><i>20</i><i>21</i><i>22</i><i>23</i><i>24</i><i>25</i><i>26</i><i>27</i><i>28</i><i>29</i><i>30</i><i>31</i></div>
    </article>

    <article class="month o2" style="left:30px;top:450px">
      <header class="tab"><span class="num">09</span><span class="name">September</span></header>
      <div class="dow"><span>Su</span><span>Mo</span><span>Tu</span><span>We</span><span>Th</span><span>Fr</span><span>Sa</span></div>
      <div class="days"><i>1</i><i>2</i><i>3</i><i>4</i><i>5</i><i>6</i><i>7</i><i>8</i><i>9</i><i>10</i><i>11</i><i>12</i><i>13</i><i>14</i><i>15</i><i>16</i><i>17</i><i>18</i><i>19</i><i>20</i><i>21</i><i>22</i><i>23</i><i>24</i><i>25</i><i>26</i><i>27</i><i>28</i><i>29</i><i>30</i></div>
    </article>
    <article class="month o4" style="left:240px;top:450px">
      <header class="tab"><span class="num">10</span><span class="name">October</span></header>
      <div class="dow"><span>Su</span><span>Mo</span><span>Tu</span><span>We</span><span>Th</span><span>Fr</span><span>Sa</span></div>
      <div class="days"><i>1</i><i>2</i><i>3</i><i>4</i><i>5</i><i>6</i><i>7</i><i>8</i><i>9</i><i>10</i><i>11</i><i>12</i><i>13</i><i>14</i><i>15</i><i>16</i><i>17</i><i>18</i><i>19</i><i>20</i><i>21</i><i>22</i><i>23</i><i>24</i><i>25</i><i>26</i><i>27</i><i>28</i><i>29</i><i>30</i><i>31</i></div>
    </article>
    <article class="month o0" style="left:450px;top:450px">
      <header class="tab"><span class="num">11</span><span class="name">November</span></header>
      <div class="dow"><span>Su</span><span>Mo</span><span>Tu</span><span>We</span><span>Th</span><span>Fr</span><span>Sa</span></div>
      <div class="days"><i>1</i><i>2</i><i>3</i><i>4</i><i>5</i><i>6</i><i>7</i><i>8</i><i>9</i><i>10</i><i>11</i><i>12</i><i>13</i><i>14</i><i>15</i><i>16</i><i>17</i><i>18</i><i>19</i><i>20</i><i>21</i><i>22</i><i>23</i><i>24</i><i>25</i><i>26</i><i>27</i><i>28</i><i>29</i><i>30</i></div>
    </article>
    <article class="month o2" style="left:660px;top:450px">
      <header class="tab"><span class="num">12</span><span class="name">December</span></header>
      <div class="dow"><span>Su</span><span>Mo</span><span>Tu</span><span>We</span><span>Th</span><span>Fr</span><span>Sa</span></div>
      <div class="days"><i>1</i><i>2</i><i>3</i><i>4</i><i>5</i><i>6</i><i>7</i><i>8</i><i>9</i><i>10</i><i>11</i><i>12</i><i>13</i><i>14</i><i>15</i><i>16</i><i>17</i><i>18</i><i>19</i><i>20</i><i>21</i><i>22</i><i>23</i><i>24</i><i>25</i><i>26</i><i>27</i><i>28</i><i>29</i><i>30</i><i>31</i></div>
    </article>
  </section>

  <footer class="footer">
    <div class="brand">COMPANYNAME</div>
    <span class="contact" style="left:292px"><svg viewBox="0 0 10 10"><rect x="2.5" y="0" width="5" height="10" rx="1"/></svg>(+123) 123 456 7890</span>
    <span class="contact" style="left:450px"><svg viewBox="0 0 10 10"><path d="M5 0 10 5H8.5V10H6V7H4V10H1.5V5H0Z"/></svg>www.companame.com</span>
    <span class="contact" style="left:630px"><svg viewBox="0 0 10 10"><path d="M0 1H10L5 9Z"/></svg>1234, City Name, Street Name, 5678</span>
  </footer>
</main>
</body>
</html>
```